Wattlegrove Campus Lodgings needs a business card design

Hi Guys,

We are a Student Accommodation company in Australia. We already have a logo which I will submit.

I will require the design of the business cards from you.

I am after something that looks clean, modern and that people feel interested and actually want to contact us.

We would like to see designs that are innovative.

On the business cards I will require to have:

Employee Name
Position
Phone number
Email
Facebook page

I hope you can help me with this project guys as I have heard really good things from you.

```html
<!DOCTYPE html>
<html lang="en">
<head>
<meta charset="utf-8">
<title>Wattlegrove Campus Lodgings – Business Card</title>
<link rel="stylesheet" href="https://fonts.googleapis.com/css2?family=Oswald:wght@600&family=PT+Sans:wght@400;700&display=swap">
<style>
  :root {
    --card-black: #1d1d1d;
    --brand-green: #13934a;
    --brand-yellow: #f6b62b;
    --text-light: #e8e8e8;
    --backdrop: #e6e2db;
  }
  * { box-sizing: border-box; margin: 0; padding: 0; }
  html, body { width: 1200px; height: 1000px; overflow: hidden; }
  body {
    background: var(--backdrop);
    font-family: "PT Sans", sans-serif;
    position: relative;
  }
  .card {
    position: absolute;
    left: 250px;
    width: 700px;
    height: 400px;
    background: var(--card-black);
    border-radius: 22px;
    overflow: hidden;
    box-shadow: 0 10px 30px rgba(0,0,0,0.25);
  }
  .card--front { top: 60px; }
  .card--back { top: 540px; }

  .brand-mark {
    flex: none;
    background: var(--brand-green);
  }
  .brand-name {
    font-family: "Oswald", sans-serif;
    font-weight: 600;
    color: var(--brand-yellow);
    text-transform: uppercase;
    line-height: 1.02;
  }
  .brand-name span { display: block; }

  /* Front */
  .brand-lockup {
    position: absolute;
    inset: 0;
    display: flex;
    align-items: center;
    justify-content: center;
    gap: 26px;
  }
  .brand-lockup .brand-mark { width: 56px; height: 56px; }
  .card--front .brand-name { font-size: 50px; letter-spacing: 1px; }

  /* Back */
  .edge-band {
    position: absolute;
    left: 0; right: 0; bottom: 0;
    height: 44px;
  }
  .edge-band__green { position: absolute; left: 0; right: 0; top: 0; height: 26px; background: var(--brand-green); }
  .edge-band__yellow { position: absolute; left: 0; right: 0; bottom: 0; height: 8px; background: var(--brand-yellow); }

  .back-brand {
    position: absolute;
    left: 48px;
    top: 48px;
    display: flex;
    align-items: center;
    gap: 14px;
  }
  .back-brand .brand-mark { width: 30px; height: 30px; }
  .back-brand .brand-name { font-size: 26px; letter-spacing: 0.5px; }

  .person {
    position: absolute;
    right: 52px;
    top: 52px;
    text-align: right;
  }
  .person__name {
    color: var(--brand-yellow);
    font-size: 22px;
    font-weight: 400;
    letter-spacing: 0.5px;
  }
  .person__title { color: var(--text-light); font-size: 16px; margin-top: 4px; }

  .contact-list {
    position: absolute;
    left: 380px;
    top: 140px;
    list-style: none;
  }
  .contact-list li {
    display: flex;
    align-items: center;
    gap: 10px;
    color: var(--text-light);
    font-size: 15px;
    line-height: 26px;
  }
  .contact-icon { width: 15px; height: 15px; flex: none; }

  .company {
    position: absolute;
    left: 48px;
    top: 240px;
    color: var(--text-light);
    font-size: 15px;
    line-height: 22px;
    font-style: normal;
  }
  .company__name {
    color: var(--brand-yellow);
    font-weight: 700;
    text-transform: uppercase;
  }
</style>
</head>
<body>

<section class="card card--front" aria-label="Card front">
  <div class="brand-lockup">
    <span class="brand-mark" aria-hidden="true"></span>
    <p class="brand-name"><span>Wattlegrove</span><span>Campus</span><span>Lodgings</span></p>
  </div>
</section>

<section class="card card--back" aria-label="Card back">
  <div class="back-brand">
    <span class="brand-mark" aria-hidden="true"></span>
    <p class="brand-name"><span>Wattlegrove</span><span>Campus</span><span>Lodgings</span></p>
  </div>

  <div class="person">
    <p class="person__name">YOUR NAME</p>
    <p class="person__title">Title</p>
  </div>

  <ul class="contact-list">
    <li>
      <svg class="contact-icon" viewBox="0 0 16 16" aria-hidden="true"><circle cx="8" cy="8" r="8" fill="var(--brand-green)"/><path d="M5 4.2l1.5-.4 1 2.2-1 .8c.5 1 1.2 1.8 2.2 2.3l.8-1 2.2 1-.4 1.5c-3 .2-6.2-3-6.3-6.4z" fill="var(--card-black)"/></svg>
      123 456 7890
    </li>
    <li>
      <svg class="contact-icon" viewBox="0 0 16 16" aria-hidden="true"><rect width="16" height="16" rx="2" fill="var(--brand-green)"/><rect x="3" y="5" width="10" height="7" fill="none" stroke="var(--card-black)" stroke-width="1.3"/><path d="M3 5l5 4 5-4" fill="none" stroke="var(--card-black)" stroke-width="1.3"/></svg>
      yourname@wattlegrove.com.au
    </li>
    <li>
      <svg class="contact-icon" viewBox="0 0 16 16" aria-hidden="true"><circle cx="8" cy="8" r="8" fill="var(--brand-green)"/><circle cx="8" cy="8" r="5" fill="none" stroke="var(--card-black)" stroke-width="1.2"/><ellipse cx="8" cy="8" rx="2.2" ry="5" fill="none" stroke="var(--card-black)" stroke-width="1.2"/><path d="M3 8h10" stroke="var(--card-black)" stroke-width="1.2"/></svg>
      www.wattlegrovelodgings.com.au
    </li>
    <li>
      <svg class="contact-icon" viewBox="0 0 16 16" aria-hidden="true"><circle cx="8" cy="8" r="8" fill="var(--brand-green)"/></svg>
      /wattlegrovelodgings
    </li>
  </ul>

  <address class="company">
    <p class="company__name">Wattlegrove Campus Lodgings</p>
    <p>Street Number, Name of Road,</p>
    <p>Sydney, AU 1234</p>
  </address>

  <div class="edge-band" aria-hidden="true">
    <span class="edge-band__green"></span>
    <span class="edge-band__yellow"></span>
  </div>
</section>

</body>
</html>
```